Larkfield Homecare - Website

MUST HAVE EXPERIENCE DESIGNING WEBSITES HEALTH CARE IN GENERAL AND/OR HOME NURSING SERVICES.

Details attached.

Number of Pages Required

1 page

Requirements
Must have
• Warm feel
caregivers

Color similar to the logo...

```html
<!DOCTYPE html>
<html lang="en">
<head>
<meta charset="utf-8">
<title>Larkfield Homecare</title>
<link href="https://fonts.googleapis.com/css2?family=Comfortaa:wght@400;700&family=Montserrat:wght@400;500;600;700&family=Roboto+Condensed:wght@300;400&family=Roboto:wght@300;400&display=swap" rel="stylesheet">
<style>
:root{
  --teal:#1a9ea6;
  --teal-2:#26c3bb;
  --teal-dark:#16838c;
  --orange:#f7841a;
  --ink:#333a45;
  --muted:#666c75;
  --navy:#2a2f5a;
  --light:#eef1f4;
  --pink-bg:#fdf7fb;
  --footer:#1f1f22;
  --white:#fff;
}
*{box-sizing:border-box;margin:0;padding:0}
html,body{width:1200px;height:3585px;overflow:hidden}
body{font-family:"Montserrat",sans-serif;color:var(--ink);background:#fff;position:relative}
section,header,footer{position:absolute;left:0;width:1200px;overflow:hidden}
.kicker{font-size:11px;text-align:center;color:#444}
.title{font-family:"Comfortaa",sans-serif;font-weight:700;color:var(--orange);font-size:22px;text-align:center}

/* top bars */
.covid{top:0;height:38px;background:var(--teal);color:#fff;font-size:11px;font-weight:600;text-align:center;line-height:38px;letter-spacing:.3px}
.infobar{top:38px;height:51px;background:var(--orange);color:#fff}
.info{position:absolute;top:10px;display:flex;gap:12px;align-items:center}
.info .ico{width:24px;height:24px;border:1.5px solid #fff;border-radius:3px;display:flex;align-items:center;justify-content:center}
.info small{display:block;font-size:9px}
.info b{font-size:11px;letter-spacing:.6px}
.toplinks{position:absolute;right:272px;top:19px;font-size:10px;font-weight:700;letter-spacing:.3px;white-space:nowrap}
.search{position:absolute;left:955px;top:14px;width:24px;height:24px;border:1.5px solid #fff;display:flex;align-items:center;justify-content:center}

/* nav */
.nav{top:89px;height:92px;background:#fff}
.brand{position:absolute;left:200px;top:30px;display:flex;align-items:center;gap:10px}
.brand .dot{width:30px;height:30px;border-radius:50%;background:var(--teal)}
.brand span{font-weight:700;font-size:18px;color:var(--teal)}
.menu{position:absolute;left:516px;top:40px;font-size:10px;font-weight:700;color:var(--teal);letter-spacing:.2px;display:flex;gap:8px;white-space:nowrap}
.menu i{font-style:normal;color:var(--teal)}

/* hero */
.hero{top:181px;height:306px;background:#f1f2f4}
.hero-photo{position:absolute;left:522px;top:0;width:512px;height:306px;background:linear-gradient(110deg,#d8d2cc 0%,#e9d6c4 40%,#6dc6c1 75%,#c9e3e1 100%)}
.hero h1{position:absolute;left:208px;top:36px;font-family:"Roboto Condensed",sans-serif;font-weight:300;color:var(--teal);font-size:38px;line-height:40px}
.hero h1 small{display:block;font-size:29px;line-height:36px}
.hero .every{position:absolute;left:206px;top:102px;font-family:"Comfortaa",sans-serif;font-weight:700;color:var(--orange);font-size:54px}
.hero p{position:absolute;left:208px;top:172px;font-size:14px;color:#333;line-height:18px}
.btn-white{position:absolute;left:208px;top:230px;width:172px;height:36px;background:#fff;font-size:11px;font-weight:600;text-align:center;line-height:36px;color:#333;box-shadow:0 1px 3px rgba(0,0,0,.08)}

/* welcome */
.welcome{top:487px;height:592px;background:#fff}
.welcome .kicker{margin-top:47px}
.welcome .title{margin-top:2px}
.welcome .text{width:680px;margin:22px auto 0;font-size:10.5px;line-height:15px;color:var(--muted);text-align:center}
.welcome .text p+p{margin-top:15px}
.svc{position:absolute;top:279px;width:137px;height:184px;border-radius:0 28px 0 28px;overflow:hidden}
.svc-label{position:absolute;top:476px;width:137px;text-align:center;font-size:11px;font-weight:600;color:var(--teal)}
.dementia{background:linear-gradient(160deg,#34b7b0,#1e9ca3);color:#fff;text-align:center;padding:22px 16px 0}
.dementia b{font-size:11px;display:block;margin-bottom:16px}
.dementia p{font-size:9px;line-height:15px}
.know{position:absolute;left:522px;top:471px;width:134px;height:36px;background:var(--orange);color:#fff;font-size:11px;font-weight:600;text-align:center;line-height:36px;border-radius:0 14px 0 14px}
.dots{position:absolute;top:528px;left:560px;display:flex;gap:12px}
.dots i{width:34px;height:3px;background:#ddd}
.dots i:first-child{background:var(--teal)}

/* missions */
.missions{top:1079px;height:310px;background:#edf1f5}
.doctor{position:absolute;left:208px;top:0;width:280px;height:310px;background:linear-gradient(180deg,#e7e2dd,#f4f4f5 70%,#dfe6ec)}
.quote-mark{font-family:Georgia,serif;font-weight:700;color:#8ec9cc;font-size:46px;line-height:1}
.missions .quote-mark{position:absolute;left:598px;top:22px}
.missions h2{position:absolute;left:600px;top:70px;font-family:"Comfortaa",sans-serif;font-weight:700;color:var(--orange);font-size:21px}
.missions .body{position:absolute;left:600px;top:107px;width:395px;font-size:10.5px;line-height:15px;color:#555}
.missions .body p+p{margin-top:14px}
.sig{position:absolute;left:600px;top:262px;font-size:10px;color:var(--teal)}
.sig-script{position:absolute;left:726px;top:250px;font-family:"Comfortaa",sans-serif;font-size:15px;color:#222}

/* why */
.why{top:1389px;height:609px;background:var(--pink-bg)}
.why .kicker{margin-top:49px}
.why .lead{width:690px;margin:26px auto 0;font-size:10.5px;line-height:15px;color:var(--muted);text-align:center}
.card{position:absolute;width:160px;height:165px;color:#fff;padding:20px 18px}
.card h3{font-size:10.5px;font-weight:500;margin-top:18px;white-space:nowrap}
.card p{font-size:9px;line-height:18px;margin-top:12px;opacity:.8}
.c1{background:linear-gradient(180deg,#7d2b86,#5c1e6b)}
.c2{background:linear-gradient(180deg,#e8353f,#f17b2b)}
.c3{background:linear-gradient(180deg,#c23494,#7b2a88)}
.c4{background:linear-gradient(180deg,#f9b81a,#f0731d)}
.c5{background:linear-gradient(180deg,#8ec840,#5ba63a)}
.c6{background:linear-gradient(160deg,#d62566,#1f6ba4)}
.c7{background:linear-gradient(180deg,#83d2d4,#1e9ba6)}
.c8{background:linear-gradient(180deg,#29b3aa,#1a8e9c)}

/* service panels */
.panels{top:1998px;height:407px}
.panel{position:absolute;top:0;height:407px;width:600px}
.panel h2{position:absolute;top:24px;font-family:"Comfortaa",sans-serif;font-weight:700;font-size:21px;line-height:26px;color:#fff}
.panel .ph{position:absolute;top:83px;width:365px;height:119px}
.panel p{position:absolute;color:#fff;font-size:10px;line-height:15px;width:320px}
.btn-outline{position:absolute;width:150px;height:32px;border:2px solid #fff;color:#fff;font-size:11px;font-weight:600;text-align:center;line-height:28px}

/* testimonials */
.testi{top:2405px;height:653px;background:#fff}
.testi .kicker{margin-top:38px}
.feature{position:absolute;left:254px;top:117px;width:348px;height:282px;background:#35bdb4;color:#fff;padding:42px 36px}
.feature h3{font-family:"Comfortaa",sans-serif;font-weight:700;font-size:26px}
.feature .role{font-family:"Roboto",sans-serif;font-weight:300;font-size:14px;margin-top:6px}
.feature blockquote{font-family:"Roboto",sans-serif;font-weight:300;font-size:13.5px;line-height:22.5px;margin:24px 0 0 20px}
.feature .q1{position:absolute;left:28px;top:110px;font-size:40px;color:#fff;font-family:Georgia,serif;font-weight:700}
.feature .q2{position:absolute;right:30px;bottom:20px;font-size:40px;color:#fff;font-family:Georgia,serif;font-weight:700}
.feature-photo{position:absolute;left:602px;top:117px;width:346px;height:282px;background:linear-gradient(135deg,#e9e3d4,#c9d7b0 50%,#f0eee8)}
.review{position:absolute;top:437px;width:200px}
.review .qm{position:absolute;left:-34px;top:-4px;font-family:Georgia,serif;font-weight:700;color:#4cc0c0;font-size:34px}
.review h4{font-family:"Comfortaa",sans-serif;font-weight:700;color:var(--navy);font-size:17px}
.review .place{font-size:11px;color:#8a8f96;margin-top:5px}
.review p{font-family:"Roboto",sans-serif;font-weight:300;font-size:13.5px;line-height:22.5px;color:#666;margin-top:18px}

/* cta */
.cta{top:3058px;height:227px;background:linear-gradient(90deg,#1aa1a7,#27c8bf)}
.cta h2{position:absolute;left:0;width:1210px;top:50px;text-align:center;font-family:"Comfortaa",sans-serif;font-weight:700;color:#fff;font-size:22px;line-height:31px}
.btn-orange{position:absolute;left:416px;top:142px;width:178px;height:36px;background:var(--orange);color:#fff;font-size:11px;font-weight:600;text-align:center;line-height:36px}
.phone-box{position:absolute;left:600px;top:142px;width:40px;height:36px;background:var(--orange);display:flex;align-items:center;justify-content:center}
.cta .call{position:absolute;left:661px;top:144px;color:#fff}
.cta .call small{display:block;font-size:9px}
.cta .call b{font-size:15px;letter-spacing:.5px}

/* footer */
.foot{top:3285px;height:300px;background:var(--footer);color:#ccc}
.foot h5{position:absolute;top:37px;font-size:10px;font-weight:700;letter-spacing:.8px;color:#fff}
.foot .addr{position:absolute;left:250px;top:70px;font-size:8.5px;line-height:22px;color:#ccc}
.foot ul{position:absolute;top:67px;list-style:none;font-size:9px;line-height:22px}
.foot li::before{content:"";display:inline-block;width:6px;height:6px;border:1.5px solid var(--teal);border-radius:50%;margin-right:9px}
.foot .nl{position:absolute;left:737px;top:37px;font-size:9px}
.foot .email{position:absolute;left:737px;top:54px;width:213px;height:34px;background:#e6f4f6;font-size:9px;color:#aab;padding:12px 12px}
.foot .signup{position:absolute;left:735px;top:98px;width:90px;height:34px;background:var(--orange);color:#fff;font-size:11px;font-weight:600;text-align:center;line-height:34px}
.foot .brand2{position:absolute;left:252px;top:172px;display:flex;align-items:center;gap:8px}
.foot .brand2 .dot{width:26px;height:26px;border-radius:50%;background:var(--orange)}
.foot .brand2 span{font-weight:700;font-size:15px;color:var(--teal)}
.copy{position:absolute;left:265px;top:268px;font-size:8.5px;color:var(--teal)}
.social{position:absolute;left:860px;top:258px;display:flex;gap:4px}
.social i{width:20px;height:20px;display:block}
</style>
</head>
<body>

<header class="covid">COVID-19 UPDATE, CLICK HERE TO KNOW ALL DETAILS</header>

<header class="infobar">
  <div class="info" style="left:220px">
    <div class="ico"><svg width="12" height="12" viewBox="0 0 24 24"><path fill="#fff" d="M6.6 10.8a15 15 0 0 0 6.6 6.6l2.2-2.2c.3-.3.7-.4 1-.2 1.1.4 2.3.6 3.6.6.6 0 1 .4 1 1V20c0 .6-.4 1-1 1A17 17 0 0 1 3 4c0-.6.4-1 1-1h3.5c.6 0 1 .4 1 1 0 1.3.2 2.5.6 3.6.1.3 0 .7-.2 1z"/></svg></div>
    <div><small>24/7 service Available</small><b>555 0142 7788 10</b></div>
  </div>
  <div class="info" style="left:411px">
    <div class="ico"><svg width="12" height="12" viewBox="0 0 24 24"><path fill="#fff" d="M11 3h2v10l4-4 1.4 1.4L12 16.8 5.6 10.4 7 9l4 4zM4 19h16v2H4z"/></svg></div>
    <div><small>Our Brochure 2021</small><b>Download Now</b></div>
  </div>
  <div class="toplinks">SERVICE REQUEST &nbsp;|&nbsp; NEWS FEED</div>
  <div class="search"><svg width="11" height="11" viewBox="0 0 24 24"><circle cx="10" cy="10" r="6" fill="none" stroke="#fff" stroke-width="3"/><path d="M15 15l6 6" stroke="#fff" stroke-width="3"/></svg></div>
</header>

<header class="nav">
  <div class="brand"><div class="dot"></div><span>Larkfield Homecare</span></div>
  <nav class="menu"><span>HOME</span><i>|</i><span>ABOUT US</span><i>|</i><span>SERVICES</span><i>|</i><span>JOIN OUR TEAM</span><i>|</i><span>TESTIMONIALS</span><i>|</i><span>CONTACT US</span></nav>
</header>

<section class="hero">
  <div class="hero-photo" role="img" aria-label="Smiling caregiver hugging an elderly woman"></div>
  <h1>Special Care<small>for your loved one</small></h1>
  <div class="every">everyday</div>
  <p>Providing quality care services<br>for over 15 years</p>
  <div class="btn-white">SERVICE REQUEST</div>
</section>

<section class="welcome">
  <div class="kicker">Welcome to</div>
  <div class="title">Larkfield Homecare</div>
  <div class="text">
    <p>Everyone should be free to experience joy and optimism in their lives, regardless of their age or condition. Larkfield Homecare provides a range of services that are tailored to meet the patient's needs, helping them to maintain their independence and live happy and fulfilling lives.</p>
    <p>Larkfield Homecare deliver comprehensive care to new born baby and mother, and elderly in the comfort of their own homes, we ensure that the needs of our clients and their families are at the heart of everything they do.<br>Provide healthcare services at the comfort of home. Medical and Nursing services to patients ranging from newborn to elderly.<br>Services are offered 24/7 and customized based on the need into hourly, daily, weekly and monthly packages.</p>
  </div>
  <div class="svc" style="left:230px;background:linear-gradient(160deg,#9fc07a,#d8c9b2 60%,#9cc8c4)" role="img" aria-label="Nurse with an elderly patient outdoors"></div>
  <div class="svc-label" style="left:230px">Cancer Care</div>
  <div class="svc" style="left:376px;background:linear-gradient(160deg,#e7d9cf,#d9a88a 60%,#ece4dd)" role="img" aria-label="Young woman sharing a moment with a senior"></div>
  <div class="svc-label" style="left:376px">Companionship</div>
  <div class="svc dementia" style="left:522px"><b>Dementia</b><p>What is dementia and how our nurse can help thepatient in an unique way. Lorem ipsum dolor sit amet esta di ania nino valencia</p></div>
  <div class="know">KNOW MORE</div>
  <div class="svc" style="left:668px;background:linear-gradient(160deg,#ede2d8,#cfb39a 55%,#b9ad9f)" role="img" aria-label="Caregiver reading with an elderly man"></div>
  <div class="svc-label" style="left:668px">Elderly Care</div>
  <div class="svc" style="left:816px;background:linear-gradient(160deg,#f2ece8,#8fd0c9 55%,#e0d6cf)" role="img" aria-label="Nurse assisting a senior woman"></div>
  <div class="svc-label" style="left:816px">Physical Disability</div>
  <div class="dots"><i></i><i></i></div>
</section>

<section class="missions">
  <div class="doctor" role="img" aria-label="Portrait of a smiling doctor with a stethoscope"></div>
  <div class="quote-mark">&ldquo;</div>
  <h2>Our Missions</h2>
  <div class="body">
    <p>It is our mission is to provide a wide variety of supportive, in-home nurse care while maintaining the highest standards in health care. Larkfield Homecare provides nursing are for both medical and non-medical services to ensure that you or your loved one is able to remain at home in a comfortable, familiar, and caring environment.</p>
    <p>Our emphasis on compassion, respect, and education, and skilled care, help make our nurses and other caregivers some of the most knowledgeable medical support staff available.</p>
  </div>
  <div class="sig">Marisol Dunbar,</div>
  <div class="sig-script">Marisol Dunbar</div>
</section>

<section class="why">
  <div class="kicker">Why Choose</div>
  <div class="title">Larkfield Homecare</div>
  <div class="lead">Provide healthcare services at the comfort of home. Medical and Nursing services to patients ranging from newborn to elderly. Services are offered 24/7 and customized based on the need into hourly, daily, weekly and monthly packages.</div>

  <div class="card c1" style="left:256px;top:196px"><svg width="30" height="32" viewBox="0 0 30 32"><circle cx="15" cy="8" r="6" fill="none" stroke="#fff" stroke-width="2.5"/><path d="M3 30v-6a8 8 0 0 1 8-8h8a8 8 0 0 1 8 8v6z" fill="#fff"/></svg><h3>Daily care experts</h3><p>We specialize in around the clock care to help seniors live well at home.</p></div>
  <div class="card c2" style="left:440px;top:196px"><svg width="32" height="32" viewBox="0 0 32 32"><circle cx="14" cy="4" r="3" fill="#fff"/><path d="M12 9v10h8l4 8M12 13a9 9 0 1 0 9 13" fill="none" stroke="#fff" stroke-width="2.5"/></svg><h3>Balanced care</h3><p>Our unique approach to care promotes healthy mind, body and spirit.</p></div>
  <div class="card c3" style="left:621px;top:196px"><svg width="32" height="32" viewBox="0 0 32 32"><circle cx="16" cy="16" r="12" fill="none" stroke="#fff" stroke-width="2.5"/><path d="M11 11c0 6 4 10 10 10l1-3-3-1-1 1c-2-1-3-2-4-4l1-1-1-3z" fill="#fff"/></svg><h3>Available 24/7</h3><p>We are available 24 hours a day to provide your loved one with a caregiver.</p></div>
  <div class="card c4" style="left:805px;top:196px"><svg width="36" height="30" viewBox="0 0 36 30"><path d="M18 28S3 19 3 10a7 7 0 0 1 15-2 7 7 0 0 1 15 2c0 9-15 18-15 18z" fill="none" stroke="#fff" stroke-width="2.5"/><path d="M6 14h7l3-5 4 9 3-4h7" fill="none" stroke="#fff" stroke-width="2"/></svg><h3>high caliber caregivers</h3><p>We typically hire only 1 in 25 applicants and provide ongoing training.</p></div>

  <div class="card c5" style="left:256px;top:382px"><svg width="36" height="30" viewBox="0 0 36 30"><path d="M3 10l6-8h18l6 8-15 18zM3 10h30M13 2l5 26 5-26" fill="none" stroke="#fff" stroke-width="2.2"/></svg><h3>Peace of mind</h3><p>Independent industry surveys place our client satisfaction rate at 97%.</p></div>
  <div class="card c6" style="left:440px;top:382px"><svg width="30" height="32" viewBox="0 0 30 32"><path d="M5 3v10a7 7 0 0 0 14 0V3M12 20v4a5 5 0 0 0 10 0v-8" fill="none" stroke="#fff" stroke-width="2.5"/><circle cx="22" cy="13" r="3" fill="none" stroke="#fff" stroke-width="2.5"/></svg><h3>A trusted partner</h3><p>Larkfield Homecare is the trusted referral choice for elder care professionals.</p></div>
  <div class="card c7" style="left:621px;top:382px"><svg width="30" height="32" viewBox="0 0 30 32"><path d="M11 2h8M12 2v10L4 28h22L18 12V2" fill="none" stroke="#fff" stroke-width="2.5"/><path d="M7 22h16l3 6H4z" fill="#fff"/></svg><h3>Cognitive therapeutics</h3><p>Fun yet effective activities designed by experts to keep aging minds sharp.</p></div>
  <div class="card c8" style="left:805px;top:382px"><svg width="30" height="32" viewBox="0 0 30 32"><circle cx="12" cy="4" r="3" fill="#fff"/><path d="M11 9l-3 10 4 4 2 8M11 9l5 6 4 0M8 19l-4 11M17 16l9 15" fill="none" stroke="#fff" stroke-width="2.4"/></svg><h3>No long term contract</h3><p>Use our services only as long as you're 100% satisfied.</p></div>
</section>

<section class="panels">
  <div class="panel" style="left:0;background:var(--orange)">
    <h2 style="left:213px">Home Nursing<br>Services</h2>
    <div class="ph" style="left:213px;background:linear-gradient(100deg,#8a7a55,#c9b99e 45%,#e6ddd3)" role="img" aria-label="Masked nurse caring for an elderly woman"></div>
    <p style="left:213px;top:220px">Looking for care, custodial care, Urinary catheterization care, Wound care, Injections, IV infusions, Vaccination or other nursing assistance? Get all of this, and more in the comfort of your home by highly qualified and experienced nurses.</p>
    <p style="left:213px;top:288px">Deliver the best choices for people who require 24-hour medical care and supervision</p>
    <div class="btn-outline" style="left:212px;top:340px">KNOW MORE</div>
  </div>
  <div class="panel" style="left:600px;background:var(--teal)">
    <h2 style="left:36px">New Born Baby &amp; Mother Care<br>At Home</h2>
    <div class="ph" style="left:33px;background:linear-gradient(100deg,#d8d5cc,#7cc1c4 45%,#7a6bb0 75%,#e8b3a0)" role="img" aria-label="Newborn baby lying on a blanket"></div>
    <p style="left:36px;top:218px">Worried about your newborn's needs? Facing issues in coping up with the initial challenges of feeding infant child and post-operative recovery? (New Born Baby &amp; Mother Care), a post-natal care program from Larkfield Homecare and enjoy the joys of motherhood without the worries.</p>
    <div class="btn-outline" style="left:41px;top:333px">KNOW MORE</div>
  </div>
</section>

<section class="testi">
  <div class="kicker">Testimonials</div>
  <div class="title">What Our Patient Says</div>
  <div class="feature">
    <h3>Nadia P.</h3>
    <div class="role">caregiving daughter</div>
    <span class="q1">&ldquo;</span>
    <blockquote>your help and assistance in this challenging period is greatly appreciated. our entire family extends our thanks for all you have done.</blockquote>
    <span class="q2">&rdquo;</span>
  </div>
  <div class="feature-photo" role="img" aria-label="Caregiver and senior woman sharing tea at a table"></div>

  <div class="review" style="left:291px"><span class="qm">&ldquo;</span><h4>Helen T.</h4><div class="place">Brookvale, ON</div><p>i am more than fully satisfied with the excellent service provided so carefully and so sincerely by each and every care giver.</p></div>
  <div class="review" style="left:528px"><span class="qm">&ldquo;</span><h4>Omar K.</h4><div class="place">Millbrook</div><p>we are confident leaving mother in Larkfield's quality care! they deliver wonderful service with a personal touch!</p></div>
  <div class="review" style="left:766px"><span class="qm">&ldquo;</span><h4>Claire W.</h4><div class="place">Caregiving daughter</div><p>my mom's primary caregiver is wonderful. the nurse is wonderful and the overall experience was awesome!</p></div>
</section>

<section class="cta">
  <h2>We do all possible things to bring<br>your peace &nbsp;of mind</h2>
  <div class="btn-orange">REQUEST FOR SERVICE</div>
  <div class="phone-box"><svg width="14" height="14" viewBox="0 0 24 24"><path fill="#fff" d="M6.6 10.8a15 15 0 0 0 6.6 6.6l2.2-2.2c.3-.3.7-.4 1-.2 1.1.4 2.3.6 3.6.6.6 0 1 .4 1 1V20c0 .6-.4 1-1 1A17 17 0 0 1 3 4c0-.6.4-1 1-1h3.5c.6 0 1 .4 1 1 0 1.3.2 2.5.6 3.6.1.3 0 .7-.2 1z"/></svg></div>
  <div class="call"><small>24/7 service available</small><b>555 0142 7788 10</b></div>
</section>

<footer class="foot">
  <h5 style="left:250px">HEADQUARTERS</h5>
  <div class="addr">418 ORCHARD LANE, SUITE 12 LARKFIELD<br>LF 20415<br>hello@larkfieldcare.example<br>555 0142 7788 10</div>
  <h5 style="left:494px">SERVICES</h5>
  <ul style="left:494px"><li>hourly care</li><li>daily care</li><li>hospital to home</li><li>respite care</li><li>specialized care</li></ul>
  <h5 style="left:616px">COMPANY</h5>
  <ul style="left:616px"><li>about us</li><li>locations</li><li>caregivers</li><li>news &amp; blog</li><li>contact us</li></ul>
  <div class="nl">sign up to receive the latest articles</div>
  <div class="email">your email address</div>
  <div class="signup">SIGN UP</div>
  <div class="brand2"><div class="dot"></div><span>Larkfield Homecare</span></div>
  <div class="copy">Copyright © 2021, Larkfield Homecare, All rights reserved</div>
  <div class="social">
    <i style="background:#1da1f2" role="img" aria-label="Social link"></i>
    <i style="background:#3b5998" role="img" aria-label="Social link"></i>
    <i style="background:#cb2027" role="img" aria-label="Social link"></i>
    <i style="background:#0e76a8" role="img" aria-label="Social link"></i>
  </div>
</footer>

</body>
</html>
```